Spielen-und-Wachsen Flyer
Zielgruppe
Eltern, die ihre Kinder in ihrer Entwicklung fördern möchten.
Aufgabenstellung
Wir organisieren eine Messe mit dem Thema "Spielen und Wachsen". Bei der Messe geht es nicht um das Lernen über Bücher (alleine) oder das Schulische, sondern die Messe soll für Eltern sein, die ihre Kinder fördern möchten durch die Behebung von Lernblockaden, Förderung der Konzentration, Kreativität, spielerisches Lernen etc. Es geht um Kinder ab ca. 4 Jahren.
Als Aussteller werden verschiedene Themen angesprochen: Kinesiologie, Logopädie, Privatschulen mit speziellem Angenbot, Schachunterricht, spielerisches Lernangebot, Kindermalen etc. , alles was darauf zielt, Kreativität und Lernen bei Kindern zu fördern.
Wir brauchen daher einen Flyer, der die Eltern anspricht. Die Messe findet am Sonntag, 9.11.2012 statt. Beginn 11 Uhr, Ende 18.00 Uhr. Ort: Seeforum - Lindenhalle, Birkenhaldeweg 5, 8047 Zürich.
Das Logo wird attached. Das Format ist frei wählbar.

```html
<!DOCTYPE html>
<html lang="de">
<head>
<meta charset="utf-8">
<title>Spielen und Wachsen – Messe Flyer</title>
<link href="https://fonts.googleapis.com/css2?family=Arimo:wght@400;700&display=swap" rel="stylesheet">
<style>
  :root {
    --orange: #f0a028;
    --purple: #952f82;
    --sky: #3ba6dd;
    --teal: #2e8c90;
    --ink: #434343;
    --band: #444444;
    --paper: #ffffff;
    --photo-a: #f3eee9;
    --photo-b: #e6dcd3;
  }
  * { margin: 0; padding: 0; box-sizing: border-box; }
  html, body { width: 1200px; height: 1200px; overflow: hidden; background: #ffffff; }
  body { position: relative; font-family: "Arimo", Arial, sans-serif; color: var(--ink); }

  .flyer { position: absolute; background: var(--paper); overflow: hidden; outline: 1px solid #e4e4e4; }
  .flyer--large { left: 71px; top: 159px; width: 604px; height: 849px; }
  .flyer--small { left: 766px; top: 228px; width: 362px; height: 711px; }

  .swatches { position: absolute; display: flex; }
  .swatches span { display: block; height: 100%; }
  .c-orange { background: var(--orange); }
  .c-purple { background: var(--purple); }
  .c-sky { background: var(--sky); }
  .c-teal { background: var(--teal); }

  .brand { position: absolute; text-align: center; color: var(--teal); font-weight: 400; }
  .brand__dot { display: block; margin: 0 auto; border-radius: 50%; background: var(--teal); }

  .title { position: absolute; right: 0; text-align: right; font-weight: 700; color: var(--ink);
           text-shadow: 1px 2px 2px rgba(0,0,0,.25); line-height: 1; white-space: nowrap; }
  .title__city { display: block; }

  .dateband { position: absolute; left: 0; right: 0; display: flex; }
  .dateband__accent { background: var(--orange); }
  .dateband__main { flex: 1; background: var(--purple); color: #fff; font-weight: 700; display: flex; flex-direction: column; justify-content: center; white-space: nowrap; }

  .hours { position: absolute; font-weight: 700; text-shadow: 1px 2px 2px rgba(0,0,0,.25); white-space: nowrap; }

  .benefits { position: absolute; list-style: none; }
  .benefits li { display: flex; align-items: center; color: var(--teal); font-weight: 700;
                 text-shadow: 1px 1px 2px rgba(0,0,0,.2); white-space: nowrap; }
  .benefits li::before { content: ""; flex: none; border-radius: 50%; background: var(--ink); }

  .photo { position: absolute; background: radial-gradient(ellipse at 50% 55%, var(--photo-b), var(--photo-a) 60%, #ffffff 85%); }

  .webband { position: absolute; left: 0; right: 0; background: var(--band); color: #fff; font-weight: 700;
             display: flex; align-items: center; justify-content: center; }

  .organizer { position: absolute; color: var(--ink); line-height: 1.5; }
  .organizer strong { display: block; font-weight: 700; }

  /* large flyer */
  .flyer--large .swatches--top { left: 0; top: 0; width: 226px; height: 85px; }
  .flyer--large .swatches--top span { width: 56.5px; }
  .flyer--large .brand { right: 38px; top: 24px; font-size: 17px; }
  .flyer--large .brand__dot { width: 40px; height: 40px; margin-bottom: 14px; }
  .flyer--large .title { top: 136px; right: 39px; font-size: 37px; }
  .flyer--large .title__city { font-size: 28px; margin-top: 8px; }
  .flyer--large .dateband { top: 226px; height: 56px; }
  .flyer--large .dateband__accent { width: 169px; }
  .flyer--large .dateband__main { padding-left: 13px; }
  .flyer--large .dateband__date { font-size: 28px; line-height: 1.05; }
  .flyer--large .dateband__place { font-size: 12.6px; margin-top: 2px; }
  .flyer--large .hours { right: 40px; top: 298px; font-size: 28px; }
  .flyer--large .benefits { left: 42px; top: 326px; }
  .flyer--large .benefits li { font-size: 22.5px; height: 37.5px; }
  .flyer--large .benefits li::before { width: 14px; height: 14px; margin-right: 20px; }
  .flyer--large .photo { left: 78px; top: 480px; width: 486px; height: 253px; }
  .flyer--large .webband { top: 733px; height: 56px; font-size: 31px; }
  .flyer--large .organizer { left: 32px; top: 807px; font-size: 9.5px; }
  .flyer--large .swatches--bottom { right: 0; top: 789px; height: 60px; }
  .flyer--large .swatches--bottom span { width: 56.5px; }

  /* small flyer */
  .flyer--small .swatches--top { left: 0; top: 0; width: 134px; height: 83px; }
  .flyer--small .swatches--top span { width: 33.5px; }
  .flyer--small .brand { right: 14px; top: 20px; font-size: 13.5px; }
  .flyer--small .brand__dot { width: 32px; height: 32px; margin-bottom: 14px; }
  .flyer--small .title { top: 117px; right: 14px; font-size: 22px; }
  .flyer--small .title__city { font-size: 19px; margin-top: 4px; }
  .flyer--small .dateband { top: 183px; height: 51px; }
  .flyer--small .dateband__accent { width: 100px; }
  .flyer--small .dateband__main { padding-left: 9px; }
  .flyer--small .dateband__date { font-size: 20.5px; line-height: 1.1; }
  .flyer--small .dateband__place { font-size: 8.2px; margin-top: 3px; }
  .flyer--small .hours { right: 14px; top: 246px; font-size: 19.5px; }
  .flyer--small .benefits { left: 20px; top: 279px; }
  .flyer--small .benefits li { font-size: 16px; height: 33.5px; }
  .flyer--small .benefits li::before { width: 10px; height: 10px; margin-right: 11px; }
  .flyer--small .photo { left: 30px; top: 425px; width: 320px; height: 182px; }
  .flyer--small .webband { top: 615px; height: 50px; font-size: 20px; }
  .flyer--small .organizer { left: 19px; top: 677px; font-size: 6.8px; }
  .flyer--small .swatches--bottom { right: 0; top: 665px; height: 46px; }
  .flyer--small .swatches--bottom span { width: 33px; }
</style>
</head>
<body>

<article class="flyer flyer--large">
  <div class="swatches swatches--top">
    <span class="c-orange"></span><span class="c-purple"></span><span class="c-sky"></span><span class="c-teal"></span>
  </div>
  <div class="brand"><span class="brand__dot"></span>Spielen und Wachsen</div>
  <h1 class="title">Spielen und Wachsen - Messe<span class="title__city">Zürich</span></h1>
  <div class="dateband">
    <div class="dateband__accent"></div>
    <div class="dateband__main">
      <span class="dateband__date">So. 9. November 2012</span>
      <span class="dateband__place">im Seeforum - Lindenhalle, Birkenhaldeweg 5, 8047 Zürich</span>
    </div>
  </div>
  <p class="hours">11-18 Uhr</p>
  <ul class="benefits">
    <li>Begabungen erkennen</li>
    <li>Konzentration fördern</li>
    <li>Lernblockaden lösen</li>
    <li>Lernen entfalten</li>
  </ul>
  <div class="photo" role="img" aria-label="Foto: zwei Kinder sitzen am Boden und spielen Schach"></div>
  <div class="webband">www.spielenundwachsen.ch</div>
  <p class="organizer"><strong>Veranstalter:</strong>SpielenundWachsen GmbH, Am Rebhang 12, 8810 Horgen</p>
  <div class="swatches swatches--bottom">
    <span class="c-teal"></span><span class="c-sky"></span><span class="c-purple"></span><span class="c-orange"></span>
  </div>
</article>

<article class="flyer flyer--small">
  <div class="swatches swatches--top">
    <span class="c-orange"></span><span class="c-purple"></span><span class="c-sky"></span><span class="c-teal"></span>
  </div>
  <div class="brand"><span class="brand__dot"></span>Spielen und Wachsen</div>
  <h1 class="title">Spielen und Wachsen - Messe<span class="title__city">Zürich</span></h1>
  <div class="dateband">
    <div class="dateband__accent"></div>
    <div class="dateband__main">
      <span class="dateband__date">So. 9. November 2012</span>
      <span class="dateband__place">im Seeforum - Lindenhalle, Birkenhaldeweg 5, 8047 Zürich</span>
    </div>
  </div>
  <p class="hours">11-18 Uhr</p>
  <ul class="benefits">
    <li>Begabungen erkennen</li>
    <li>Konzentration fördern</li>
    <li>Lernblockaden lösen</li>
    <li>Lernen entfalten</li>
  </ul>
  <div class="photo" role="img" aria-label="Foto: zwei Kinder sitzen am Boden und spielen Schach"></div>
  <div class="webband">www.spielenundwachsen.ch</div>
  <p class="organizer"><strong>Veranstalter:</strong>SpielenundWachsen GmbH, Am Rebhang 12, 8810 Horgen</p>
  <div class="swatches swatches--bottom">
    <span class="c-teal"></span><span class="c-sky"></span><span class="c-purple"></span><span class="c-orange"></span>
  </div>
</article>

</body>
</html>
```